The Velvet Lintel with an elephant incorporated in the background

Target Market(s)

Real estate

Industry/Entity Type

Real Estate

Contact Information for Business Card

On back on want my name & number
In front I want the business name, "the velvet lintel", below to say staging & design

Logo Text

The Velvet Lintel

Font styles to use
Serif

Colors
000000

Requirements
Must have
• I want an elephant behind the writing in gold transperant

```html
<!DOCTYPE html>
<html lang="en">
<head>
<meta charset="utf-8">
<title>The Velvet Lintel – Business Card</title>
<link href="https://fonts.googleapis.com/css2?family=Open+Sans:wght@400;600&family=Rubik:wght@900&display=swap" rel="stylesheet">
<style>
  :root {
    --backdrop: #2a2a2a;
    --card: #1f1f1f;
    --gold: #b59a4e;
    --white: #f4f4f4;
    --elephant-faint: rgba(120, 104, 70, 0.35);
  }
  * { box-sizing: border-box; margin: 0; padding: 0; }
  html, body {
    width: 1200px; height: 1000px; overflow: hidden;
    background: var(--backdrop);
  }
  .canvas {
    position: relative; width: 1200px; height: 1000px;
  }
  .card {
    position: absolute; left: 250px; width: 700px; height: 400px;
    background: var(--card);
    box-shadow: 0 12px 30px rgba(0,0,0,0.45);
    overflow: hidden;
  }
  .card--front { top: 60px; }
  .card--back { top: 540px; }

  /* front */
  .elephant-watermark {
    position: absolute; left: 200px; top: 0; width: 300px; height: 380px;
    background: radial-gradient(ellipse at 50% 40%, var(--elephant-faint), rgba(120,104,70,0.08) 70%, transparent 80%);
  }
  .wordmark-frame {
    position: absolute; left: 50%; top: 50%;
    transform: translate(-50%, -50%);
    border: 2px solid var(--white);
    padding: 18px 26px;
    white-space: nowrap;
  }
  .wordmark {
    font-family: "Open Sans", sans-serif;
    font-weight: 400; font-size: 17px;
    letter-spacing: 0.42em; text-transform: uppercase;
    color: var(--white);
  }

  /* back */
  .business-line {
    position: absolute; left: 48px; top: 52px;
    font-family: "Rubik", sans-serif; font-weight: 900;
    font-size: 22px; letter-spacing: 0.02em; text-transform: uppercase;
    color: var(--gold);
  }
  .contact {
    position: absolute; left: 58px; top: 268px;
    border-left: 3px solid var(--gold);
    padding-left: 12px;
  }
  .contact__name {
    font-family: "Open Sans", sans-serif; font-weight: 600;
    font-size: 30px; letter-spacing: 0.04em; text-transform: uppercase;
    color: var(--gold); line-height: 1.1;
  }
  .contact__phone {
    font-family: "Open Sans", sans-serif; font-weight: 400;
    font-size: 17px; color: var(--white); margin-top: 2px;
  }
  .elephant-figure {
    position: absolute; left: 470px; top: 230px; width: 200px; height: 140px;
    border-radius: 40% 50% 30% 30%;
    background: radial-gradient(ellipse at 45% 50%, #e2c25a, #b08a2c 60%, rgba(120,90,30,0.6) 80%, transparent 90%);
  }
</style>
</head>
<body>
<main class="canvas">
  <section class="card card--front">
    <div class="elephant-watermark" role="img" aria-label="Faint gold elephant illustration facing forward"></div>
    <div class="wordmark-frame"><span class="wordmark">The Velvet Lintel</span></div>
  </section>

  <section class="card card--back">
    <h1 class="business-line">The Velvet Lintel, Staging &amp; Design</h1>
    <div class="contact">
      <p class="contact__name">Corin Hale</p>
      <p class="contact__phone">+000 555 014 227</p>
    </div>
    <div class="elephant-figure" role="img" aria-label="Gold elephant figurine with raised trunk"></div>
  </section>
</main>
</body>
</html>
```